Sports / Entertainment Media Co needs a biz card design

We are a media co / luxury lifestyle brand that targets professional athletes, entertainers and high net-worth fans. We are currently preparing for a relaunch and in need for new biz cards. I envision a black on black card with a pop of color on opposite side. Color Palette black, white, red etc. I want this card to exude sexiness and power. Very high stylized, hip and cool. I have attached the logo - I would like to see it all in black, but also open to other ideas. I will also upload a current card with all information needed on this new card. Furthermore I will add some samples of other cards I love. Thanks!!!

I provided suggestions, however I am open to all ideas!!   Be as creative as you can.  Think cutting-edge, sexy and powerful.  Take a look at the cards I uploaded to get a sense for what I like.  Thanks!!!

Industry/Entity Type

Entertainment

```html
<!DOCTYPE html>
<html lang="en">
<head>
<meta charset="utf-8">
<title>Strides Business Card</title>
<link href="https://fonts.googleapis.com/css2?family=Exo+2:wght@400;500&family=Roboto:wght@700&family=Saira+Condensed:wght@500;700&display=swap" rel="stylesheet">
<style>
  :root {
    --backdrop: #1c1c1e;
    --card-black: #050505;
    --card-white: #f4f4f4;
    --brand-red: #ee0a0a;
    --name-red: #8a0d0d;
    --ink: #111111;
    --muted: #5c5c5c;
    --light-text: #ffffff;
  }
  * { margin: 0; padding: 0; box-sizing: border-box; }
  html, body { width: 1200px; height: 863px; overflow: hidden; }
  body { background: var(--backdrop); position: relative; }

  .card {
    position: absolute;
    width: 560px;
    height: 320px;
    overflow: hidden;
    box-shadow: 0 18px 40px rgba(0,0,0,.55);
  }

  /* Front side */
  .card--front { left: 90px; top: 110px; background: var(--card-black); }
  .front-panel {
    position: absolute; left: 118px; top: 42px; width: 318px; height: 170px;
    background: var(--card-white);
  }
  .wordmark {
    position: absolute;
    font-family: "Roboto", Arial, sans-serif;
    font-weight: 700;
    color: var(--ink);
    letter-spacing: -1px;
    line-height: 1;
  }
  .wordmark-domain {
    position: absolute;
    font-family: "Exo 2", Arial, sans-serif;
    font-size: 9px;
    color: var(--muted);
  }
  .front-panel .wordmark { left: 28px; top: 50px; font-size: 58px; }
  .front-panel .wordmark-domain { left: 32px; top: 112px; }
  .front-web {
    position: absolute; left: 228px; top: 242px;
    font-family: "Exo 2", Arial, sans-serif; font-size: 13px;
    color: var(--light-text); letter-spacing: .5px;
  }

  /* Back side */
  .card--back { left: 550px; top: 433px; background: var(--card-white); }
  .back-shapes { position: absolute; inset: 0; }
  .card--back .wordmark { left: 30px; top: 150px; font-size: 52px; }
  .card--back .wordmark-domain { left: 34px; top: 206px; }

  .holder { position: absolute; left: 262px; top: 62px; }
  .holder-name {
    font-family: "Saira Condensed", Arial, sans-serif; font-weight: 700;
    font-size: 30px; color: var(--name-red); letter-spacing: 1px; line-height: 1;
  }
  .holder-role {
    font-family: "Saira Condensed", Arial, sans-serif; font-weight: 500;
    font-size: 13px; color: var(--name-red); letter-spacing: 2px; margin-top: 2px;
  }

  .contact-list { position: absolute; left: 288px; top: 150px; list-style: none; }
  .contact-item { display: flex; align-items: center; height: 52px; }
  .contact-icon { width: 26px; height: 26px; flex: none; margin-right: 18px; }
  .contact-text {
    font-family: "Exo 2", Arial, sans-serif; font-size: 13px;
    color: var(--light-text); line-height: 1.25; letter-spacing: .3px;
  }
</style>
</head>
<body>

  <section class="card card--front" aria-label="Business card front">
    <div class="front-panel">
      <span class="wordmark">strides</span>
      <span class="wordmark-domain">stridemag.com</span>
    </div>
    <p class="front-web">www.stridesmag.com</p>
  </section>

  <section class="card card--back" aria-label="Business card back">
    <svg class="back-shapes" width="560" height="320" viewBox="0 0 560 320" aria-hidden="true">
      <polygon points="215,0 560,0 560,320 300,320 270,128 215,128" fill="var(--card-black)"/>
      <polygon points="225,66 560,30 560,104 250,132 225,120" fill="var(--brand-red)"/>
    </svg>

    <span class="wordmark">strides</span>
    <span class="wordmark-domain">stridemag.com</span>

    <div class="holder">
      <p class="holder-name">ADRIAN COLE</p>
      <p class="holder-role">GENERAL MANAGER</p>
    </div>

    <ul class="contact-list">
      <li class="contact-item">
        <svg class="contact-icon" viewBox="0 0 26 26" aria-hidden="true">
          <circle cx="13" cy="13" r="13" fill="#fff"/>
          <path d="M13 6a5 5 0 0 0-5 5c0 4 5 9 5 9s5-5 5-9a5 5 0 0 0-5-5z" fill="#111"/>
          <circle cx="13" cy="11" r="1.8" fill="#fff"/>
        </svg>
        <p class="contact-text">42 Harbor Lane Road,<br>5th floor Suite B.</p>
      </li>
      <li class="contact-item">
        <svg class="contact-icon" viewBox="0 0 26 26" aria-hidden="true">
          <circle cx="13" cy="13" r="13" fill="#fff"/>
          <path d="M6 11c0-2 3-3.5 7-3.5s7 1.5 7 3.5v1h-3.5v-1.5h-7V12H6z" fill="#111"/>
          <rect x="8" y="13" width="10" height="6" rx="1" fill="#111"/>
        </svg>
        <p class="contact-text">012 555 0147<br>012 555 0147</p>
      </li>
      <li class="contact-item">
        <svg class="contact-icon" viewBox="0 0 26 26" aria-hidden="true">
          <circle cx="13" cy="13" r="13" fill="#fff"/>
          <g fill="none" stroke="#111" stroke-width="1.4">
            <circle cx="13" cy="13" r="7"/>
            <ellipse cx="13" cy="13" rx="3" ry="7"/>
            <line x1="6" y1="13" x2="20" y2="13"/>
            <line x1="7.5" y1="9.5" x2="18.5" y2="9.5"/>
            <line x1="7.5" y1="16.5" x2="18.5" y2="16.5"/>
          </g>
        </svg>
        <p class="contact-text">hello@stridesmag.com<br>www.stridesmag.com</p>
      </li>
    </ul>
  </section>

</body>
</html>
```